Marvista Coffee Roasters needs a coffee bag design for retail sales

We need an outstanding design for a retail coffee bag to package our outstanding craft roasted coffee beans. We have our logo and need to incorporate that into an original, overall design that includes areas for text boxes on the front, back and sides. We can provide the text when we select the design. One text box on the front will remain blank. This is where we will adhere a label that will describe the particular coffee in the package. And blank text box on the back to print a bar code.
These are our preliminary thoughts and are open minded to other options.

We would like a clean, "classy" design (think wine label). We are not sold on any particular color at this time for the bag or for the text but would design to work on different color bags(pleasing, eyecatching). We want the design to convey that our coffee is an exceptional product -- creative, sustainable, organic, socially and environmentally responsible and with remarkable taste.
Updates

I hope you understand that we are not trying to create a new label. We want to get the bags printed with a design that includes our logo. The design would need a space on the front for a small sticker or label that we can print ourselves giving the origin or blend of each particular coffee.(text only) I like the idea you showed us of the back text box with the rough edge like our logo. We wont print bar codes on the bags. if needed we will affix bar code stickers to the bottom of the bag. There is a website that has a template for creating bag designs.  You can access the templates by creating a free account. We would use the 12/16 oz gusseted bags. Here is a link. http://www.pouchwerk.example/

Target Market(s)

sophisticated coffee drinkers ---similar to wine connoiseurs

Industry/Entity Type

Retail

Requirements
Must have
• our Logo --font is Trajen Pro --- except for the J...which was created to have the up-curl
Nice to have
• something unique
Should not have
• goofy cartoon-like cliche--common coffee related images and colors

```html
<!DOCTYPE html>
<html lang="en">
<head>
<meta charset="utf-8">
<title>Marvista Coffee Roasters — Retail Bag Front</title>
<link rel="stylesheet" href="https://fonts.googleapis.com/css2?family=Cinzel:wght@400;500;700&display=swap">
<style>
  :root {
    --backdrop: #1b1b1b;
    --bag-green: #22b83c;
    --bag-green-light: #44d95b;
    --bag-green-mid: #2fc748;
    --bag-green-dark: #148c28;
    --ink: #0c1f10;
    --label-paper: #fbfbf6;
    --label-ink: #151515;
    --net-white: #f4fff4;
  }
  * { margin: 0; padding: 0; box-sizing: border-box; }
  html, body {
    width: 1200px;
    height: 797px;
    overflow: hidden;
    background: var(--backdrop);
  }
  .canvas {
    position: relative;
    width: 1200px;
    height: 797px;
    background: var(--backdrop);
  }
  .bag-front {
    position: absolute;
    left: 480px;
    top: 54px;
    width: 240px;
    height: 690px;
  }
  .bag-surface {
    position: absolute;
    inset: 0;
    background:
      radial-gradient(ellipse 70% 30% at 70% 20%, rgba(20,140,40,0.35), transparent 70%),
      radial-gradient(ellipse 70% 30% at 30% 55%, rgba(20,140,40,0.3), transparent 70%),
      radial-gradient(ellipse 70% 25% at 65% 85%, rgba(20,140,40,0.3), transparent 70%),
      linear-gradient(90deg,
        var(--bag-green-dark) 0%,
        var(--bag-green) 12%,
        var(--bag-green-light) 45%,
        var(--bag-green-mid) 78%,
        var(--bag-green-dark) 100%);
  }
  .bag-crimp {
    position: absolute;
    left: 0;
    top: 0;
    width: 100%;
    height: 16px;
    background: var(--bag-green-dark);
    opacity: 0.6;
  }
  .brand-name {
    position: absolute;
    writing-mode: vertical-rl;
    transform: rotate(180deg);
    font-family: "Cinzel", serif;
    font-weight: 400;
    color: var(--ink);
    white-space: nowrap;
    line-height: 1;
    text-transform: uppercase;
  }
  .brand-name--primary {
    left: 60px;
    top: 122px;
    font-size: 50px;
    letter-spacing: 1px;
  }
  .brand-name--secondary {
    left: 136px;
    top: 100px;
    font-size: 26px;
    letter-spacing: 0.5px;
  }
  .brand-square {
    position: absolute;
    left: 70px;
    top: 420px;
    width: 100px;
    height: 100px;
    background: var(--ink);
    border: 4px solid var(--label-paper);
  }
  .coffee-label {
    position: absolute;
    left: 20px;
    top: 534px;
    width: 200px;
    height: 72px;
    background: var(--label-paper);
    color: var(--label-ink);
    font-family: "Cinzel", serif;
    text-align: center;
    padding-top: 9px;
  }
  .coffee-label__title {
    font-size: 14px;
    line-height: 1.2;
  }
  .coffee-label__note {
    font-size: 11px;
    margin-top: 4px;
    letter-spacing: 0.5px;
  }
  .net-weight {
    position: absolute;
    left: 0;
    top: 640px;
    width: 100%;
    text-align: center;
    font-family: "Cinzel", serif;
    font-size: 14px;
    font-weight: 700;
    color: var(--net-white);
    white-space: nowrap;
  }
</style>
</head>
<body>
  <main class="canvas">
    <section class="bag-front">
      <div class="bag-surface" role="img" aria-label="Glossy green foil bag face with faint tone-on-tone swirl pattern"></div>
      <div class="bag-crimp"></div>

      <div class="brand-name brand-name--primary">Marvista</div>
      <div class="brand-name brand-name--secondary">Coffee Roasters</div>
      <div class="brand-square"></div>

      <div class="coffee-label">
        <p class="coffee-label__title">PREMIUM DARK COFFEE<br>ROASTED</p>
        <p class="coffee-label__note">100% NATURAL</p>
      </div>

      <p class="net-weight">NET WT 12oz (340g)</p>
    </section>
  </main>
</body>
</html>
```